Business Card Redesign

We would like to redesign our existing business cards.
The new design shall look:
ELEGANT, LUXURY, PROFESSIONAL
Reference:
YOU CAN VISIT WWW.LUMEN-BRIDGE-PARTNERS.EXAMPLE FOR BETTER UNDERSTANDING OF COMPANY STRATEGY AND POSITION
Additional:
CHOSEN CANDIDATE SHALL PROVIDE THE INSTRUCTION OF PRINTING IF ANY THERMAL COVERAGE OR ANY ADDITION IS OFFERED
Industry/Entity Type
Business

```html
<!DOCTYPE html>
<html lang="en">
<head>
<meta charset="utf-8">
<title>Lumen Bridge Partners – Business Cards</title>
<link rel="stylesheet" href="https://fonts.googleapis.com/css2?family=Tinos:wght@400;700&family=Noto+Sans+TC:wght@400;500&display=swap">
<style>
  :root {
    --page: #e6e2dc;
    --gold: #e8a514;
    --gold-light: #f1c25c;
    --navy: #1d5496;
    --navy-light: #6f9bd1;
    --steel-1: #c9cbcd;
    --steel-2: #f2f3f4;
    --steel-3: #a9acaf;
    --ink: #3a3b3d;
    --white: #ffffff;
  }
  * { margin: 0; padding: 0; box-sizing: border-box; }
  html, body { width: 1183px; height: 1200px; overflow: hidden; }
  body {
    background: var(--page);
    font-family: "Tinos", "Times New Roman", serif;
    position: relative;
  }
  .card {
    position: absolute;
    left: 161px;
    width: 860px;
    height: 516px;
    border-radius: 40px;
    overflow: hidden;
    background:
      repeating-linear-gradient(155deg, rgba(255,255,255,0.10) 0 2px, rgba(0,0,0,0.03) 2px 5px),
      linear-gradient(120deg, var(--steel-3) 0%, var(--steel-1) 22%, var(--steel-2) 42%, var(--steel-1) 58%, var(--steel-2) 76%, var(--steel-3) 100%);
    box-shadow: 0 6px 18px rgba(0,0,0,0.18);
  }
  .card--english { top: 56px; }
  .card--chinese { top: 628px; }
  .card__band { position: absolute; inset: 0; width: 100%; height: 100%; }

  .identity {
    position: absolute;
    right: 56px;
    top: 40px;
    text-align: right;
    color: var(--white);
  }
  .identity__name { font-size: 36px; font-weight: 700; line-height: 1.1; }
  .identity__role { font-size: 23px; }
  .card--chinese .identity { font-family: "Noto Sans TC", sans-serif; }
  .card--chinese .identity__name { font-size: 40px; font-weight: 500; }
  .card--chinese .identity__role { font-size: 24px; }

  .company {
    position: absolute;
    left: 56px;
    top: 150px;
    display: flex;
    align-items: center;
    gap: 22px;
  }
  .company__dot {
    width: 150px;
    height: 150px;
    border-radius: 50%;
    background: var(--navy);
    flex: none;
  }
  .company__name {
    color: var(--navy);
    font-size: 30px;
    font-weight: 700;
    line-height: 1.2;
    letter-spacing: 1px;
  }
  .card--chinese .company { top: 110px; }

  .address {
    position: absolute;
    left: 56px;
    bottom: 48px;
    color: var(--ink);
    font-size: 21px;
    line-height: 1.3;
  }
  .address__title { color: var(--navy); font-size: 25px; margin-bottom: 4px; }
  .card--chinese .address { font-family: "Noto Sans TC", sans-serif; font-size: 22px; }
  .card--chinese .address__title { font-size: 26px; }

  .contacts {
    position: absolute;
    right: 48px;
    bottom: 40px;
    list-style: none;
    color: var(--ink);
    font-size: 24px;
    line-height: 1.5;
  }
  .contacts__item { display: flex; justify-content: flex-end; align-items: center; gap: 10px; }
  .contacts__icon { width: 20px; height: 20px; flex: none; fill: var(--navy); }
</style>
</head>
<body>

<section class="card card--english" aria-label="Business card, English side">
  <svg class="card__band" viewBox="0 0 860 516" preserveAspectRatio="none" aria-hidden="true">
    <defs>
      <linearGradient id="goldEn" x1="0" y1="0" x2="1" y2="0">
        <stop offset="0" stop-color="#e6a21a"/>
        <stop offset="0.45" stop-color="#f2c461"/>
        <stop offset="1" stop-color="#e6a010"/>
      </linearGradient>
    </defs>
    <path d="M0 0 H860 V290 C 690 170, 420 70, 0 80 Z" fill="url(#goldEn)"/>
    <path d="M0 88 C 420 76, 690 176, 860 296" fill="none" stroke="var(--navy-light)" stroke-width="5"/>
    <path d="M0 98 C 420 88, 690 188, 860 312" fill="none" stroke="var(--navy)" stroke-width="14"/>
  </svg>

  <div class="identity">
    <p class="identity__name">Elena Vos</p>
    <p class="identity__role">PR Consultant</p>
  </div>

  <div class="company">
    <span class="company__dot"></span>
    <p class="company__name">LUMEN BRIDGE<br>PARTNERS LIMITED</p>
  </div>

  <div class="address">
    <p class="address__title">Headquarters (Hong Kong)</p>
    <p>Rm. 1203B, 12/F, Harbourline Centre,</p>
    <p>18 Lantern Street, Central, Hong Kong</p>
  </div>

  <ul class="contacts">
    <li class="contacts__item"><svg class="contacts__icon" viewBox="0 0 20 20"><path d="M5 2l3 4-2 2c1 2 3 4 5 5l2-2 4 3-2 3C9 17 3 11 2 5z"/></svg>(852) 3904-1128</li>
    <li class="contacts__item"><svg class="contacts__icon" viewBox="0 0 20 20"><path d="M6 1h8v18H6zM8 4v6h4V4z"/></svg>(852) 6718 4402</li>
    <li class="contacts__item"><svg class="contacts__icon" viewBox="0 0 20 20"><path d="M5 3h8v5h4v9H3V8h2zM7 5v3h4V5zM6 11v2h3v-2zm5 0v2h3v-2z"/></svg>(852) 3904-1130</li>
    <li class="contacts__item"><svg class="contacts__icon" viewBox="0 0 20 20"><path d="M1 4h18v12H1zm2 2v1l7 5 7-5V6l-7 5z"/></svg>elena@lumen-bridge-partners.example</li>
    <li class="contacts__item"><svg class="contacts__icon" viewBox="0 0 20 20"><path d="M10 1a9 9 0 100 18 9 9 0 000-18zm0 2c1 1 2 3 2 6H8c0-3 1-5 2-6zM3 9h3c0-2 .5-4 1.5-5.5A7 7 0 003 9zm11 0h3a7 7 0 00-4.5-5.5C13.5 5 14 7 14 9zM3 11a7 7 0 004.5 5.5C6.5 15 6 13 6 11zm5 0c0 3 1 5 2 6 1-1 2-3 2-6zm6 0c0 2-.5 4-1.5 5.5A7 7 0 0017 11z"/></svg>www.lumen-bridge-partners.example</li>
  </ul>
</section>

<section class="card card--chinese" aria-label="Business card, Chinese side" lang="zh-Hant">
  <svg class="card__band" viewBox="0 0 860 516" preserveAspectRatio="none" aria-hidden="true">
    <defs>
      <linearGradient id="goldZh" x1="0" y1="0" x2="1" y2="0">
        <stop offset="0" stop-color="#e6a21a"/>
        <stop offset="0.5" stop-color="#f2c461"/>
        <stop offset="1" stop-color="#e6a010"/>
      </linearGradient>
    </defs>
    <path d="M0 0 H860 V300 C 640 180, 380 40, 0 40 Z" fill="url(#goldZh)"/>
    <path d="M0 48 C 380 48, 640 188, 860 308" fill="none" stroke="var(--navy-light)" stroke-width="5"/>
    <path d="M0 58 C 380 60, 640 200, 860 324" fill="none" stroke="var(--navy)" stroke-width="14"/>
  </svg>

  <div class="identity">
    <p class="identity__name">溫雅晴</p>
    <p class="identity__role">公關顧問</p>
  </div>

  <div class="company">
    <span class="company__dot"></span>
    <p class="company__name">LUMEN BRIDGE<br>PARTNERS LIMITED</p>
  </div>

  <div class="address">
    <p class="address__title">香港總部</p>
    <p>香港中環燈籠街 18 號</p>
    <p>海濱中心 12 樓 1203B</p>
  </div>

  <ul class="contacts">
    <li class="contacts__item"><svg class="contacts__icon" viewBox="0 0 20 20"><path d="M5 2l3 4-2 2c1 2 3 4 5 5l2-2 4 3-2 3C9 17 3 11 2 5z"/></svg>(852) 3904-1128</li>
    <li class="contacts__item"><svg class="contacts__icon" viewBox="0 0 20 20"><path d="M6 1h8v18H6zM8 4v6h4V4z"/></svg>(852) 6718 4402</li>
    <li class="contacts__item"><svg class="contacts__icon" viewBox="0 0 20 20"><path d="M5 3h8v5h4v9H3V8h2zM7 5v3h4V5zM6 11v2h3v-2zm5 0v2h3v-2z"/></svg>(852) 3904-1130</li>
    <li class="contacts__item"><svg class="contacts__icon" viewBox="0 0 20 20"><path d="M1 4h18v12H1zm2 2v1l7 5 7-5V6l-7 5z"/></svg>elena@lumen-bridge-partners.example</li>
    <li class="contacts__item"><svg class="contacts__icon" viewBox="0 0 20 20"><path d="M10 1a9 9 0 100 18 9 9 0 000-18zm0 2c1 1 2 3 2 6H8c0-3 1-5 2-6zM3 9h3c0-2 .5-4 1.5-5.5A7 7 0 003 9zm11 0h3a7 7 0 00-4.5-5.5C13.5 5 14 7 14 9zM3 11a7 7 0 004.5 5.5C6.5 15 6 13 6 11zm5 0c0 3 1 5 2 6 1-1 2-3 2-6zm6 0c0 2-.5 4-1.5 5.5A7 7 0 0017 11z"/></svg>www.lumen-bridge-partners.example</li>
  </ul>
</section>

</body>
</html>
```